Vereins Website
Zielgruppe
Webiste für den Verein 'Katzenhain Oberlau' (details siehe Anhang).
Ziel der Website:
- Sponsoren finden
- Vereinsmitglieder finden & Interessen bündeln.
Aufgabenstellung
Die Webiste sollt aufgeräumt, übersichtlich und freundlich wirken.

```html
<!DOCTYPE html>
<html lang="de">
<head>
<meta charset="utf-8">
<title>Verein Katzenhain Oberlau</title>
<link href="https://fonts.googleapis.com/css2?family=Montserrat:wght@400;500;600;700&family=Roboto:wght@500&display=swap" rel="stylesheet">
<style>
:root{
  --orange:#f3a233;
  --orange-soft:#f1b95c;
  --text:#555;
  --dark:#222;
  --cream:#fcf1ea;
  --footer:#4a3b30;
  --line:#cfcfcf;
}
*{box-sizing:border-box;margin:0;padding:0}
html,body{width:1200px;height:3125px;overflow:hidden;background:#fff}
body{position:relative;font-family:'Montserrat',sans-serif;color:var(--text)}
.abs{position:absolute}
.site-header{left:0;top:0;width:1200px;height:58px;background:#fff;border-bottom:1px solid #eee}
.brand{left:260px;top:8px;display:flex;align-items:center;gap:8px;font-weight:700;font-size:11px;line-height:12px;color:var(--dark)}
.brand-dot{width:22px;height:22px;border-radius:50%;background:var(--orange)}
.nav{left:718px;top:23px;display:flex;gap:30px;font-size:11px;font-weight:500;color:var(--dark);letter-spacing:.3px}
.hero{left:0;top:58px;width:1200px;height:513px;background:linear-gradient(180deg,#6f8a4a 0%,#8fa85a 45%,#6e9a34 75%,#5b8a2a 100%)}
.hero-title{left:0;top:238px;width:1200px;text-align:center;color:#fff;font-weight:700;font-size:41px;line-height:44px;text-shadow:0 2px 6px rgba(0,0,0,.45)}
.btn{background:var(--orange);color:#fff;font-weight:600;text-align:center}
.hero-btn{top:364px;height:35px;line-height:35px;font-size:15px}
.sec-title{width:1200px;left:0;text-align:center;font-family:'Roboto',sans-serif;font-weight:500;font-size:27px;color:var(--dark);display:flex;justify-content:center;align-items:center;gap:10px}
.about-text{left:260px;top:724px;width:686px;font-size:15px;letter-spacing:.3px;line-height:17.6px;text-align:justify;color:#666}
.about-text p+p{margin-top:17px}
.photo{left:0;width:1200px}
.kicker{font-size:11.5px;font-weight:500;color:var(--orange);letter-spacing:.2px}
.member-text{left:69px;top:1548px;width:465px;font-size:11.7px;line-height:18.3px;text-align:justify;color:#555}
.member-text p+p{margin-top:18px}
.member-text strong{color:var(--dark);font-weight:600}
.field{border:1px solid var(--line);border-radius:2px;background:#fff;height:27px;font-size:9.5px;color:#999;padding:8px 9px;font-family:Arial,sans-serif}
.small-btn{font-size:10px;height:27px;line-height:27px;border-radius:2px}
.sponsor-band{left:0;top:1957px;width:1200px;height:300px;background:var(--cream)}
.logo-box{top:2109px;height:84px;width:125px;background:#fff;display:flex;align-items:center;justify-content:center;font-weight:700;font-size:14px;color:var(--dark)}
.logo-box.empty{background:var(--orange-soft);font-size:11px;font-weight:500;line-height:13px;text-align:center}
.bank{left:406px;top:2400px;font-size:17px;line-height:20.5px;color:#333;letter-spacing:.3px}
.bank b{font-weight:700;color:var(--dark)}
.pay{top:2506px;height:36px;display:flex;align-items:center;gap:6px;font-weight:600;font-size:12px;color:var(--dark)}
.pay-mark{width:10px;height:10px;background:var(--orange)}
.pay-slip{left:682px;top:2508px;width:123px;height:33px;line-height:33px;background:var(--orange-soft);color:#333;font-size:9.5px;font-weight:500;text-align:center}
.contact-photo{top:2622px;height:254px;background:linear-gradient(180deg,#8a5a3a 0%,#a0714e 50%,#6f7a3a 100%)}
.contact-title{left:0;top:2735px;width:1200px;text-align:center;color:#fff;font-weight:700;font-size:29px;text-shadow:0 2px 6px rgba(0,0,0,.45)}
.footer{left:0;top:3089px;width:1200px;height:36px;background:var(--footer);color:#fff;font-size:11px;text-align:center;line-height:36px}
</style>
</head>
<body>
<header class="abs site-header">
  <div class="abs brand"><span class="brand-dot"></span><span>Verein<br>Katzenhain Oberlau</span></div>
  <nav class="abs nav"><span>MITGLIED</span><span>SPONSOR</span><span>KONTAKT</span></nav>
</header>

<section class="abs hero" role="img" aria-label="Foto eines Hundes, der über eine sonnige Wiese rennt"></section>
<h1 class="abs hero-title">Lorem ipsum dolor sit amet mit<br>Verein Katzenhain Oberlau</h1>
<div class="abs btn hero-btn" style="left:391px;width:183px">MITGLIED WERDEN</div>
<div class="abs btn hero-btn" style="left:631px;width:186px">SPONSOR WERDEN</div>

<h2 class="abs sec-title" style="top:652px">
  <svg width="48" height="26" viewBox="0 0 48 26" aria-hidden="true"><path d="M7 3a5 5 0 0 1 8 3h18a5 5 0 1 1 8 4 5 5 0 0 1 0 6 5 5 0 1 1-8 4H15a5 5 0 1 1-8-4 5 5 0 0 1 0-6 5 5 0 0 1 0-7z" fill="none" stroke="var(--orange)" stroke-width="4"/></svg>
  Verein Katzenhain Oberlau
</h2>
<div class="abs about-text">
  <p>Nach dem Vorbild von Eiken möchten wir in Oberlau eine eingezäunte Hundespielwiese auf die Beine stellen und damit das Wohlergehen der Hunde fördern.Auf der eingezäunten Wiese können die Hunde ohne Leinenzwang spielen, sich austoben und sozialisieren.Gleichzeitig schafft dies einen Raum, in dem sich die Hundehalter treffen und austauschen können.</p>
  <p>Ein Begegnungsort für die ganze Region, von dem alle profitieren.</p>
</div>

<section class="abs photo" style="top:916px;height:397px;background:linear-gradient(90deg,#b8c6c8 0%,#a9b8bc 40%,#5a6e8a 55%,#d8c49a 75%,#8fae4a 100%)" role="img" aria-label="Foto einer Person, die einen hellen Hund auf der Wiese streichelt"></section>

<h2 class="abs sec-title" style="top:1426px">
  <svg width="48" height="26" viewBox="0 0 48 26" aria-hidden="true"><path d="M7 3a5 5 0 0 1 8 3h18a5 5 0 1 1 8 4 5 5 0 0 1 0 6 5 5 0 1 1-8 4H15a5 5 0 1 1-8-4 5 5 0 0 1 0-6 5 5 0 0 1 0-7z" fill="none" stroke="var(--orange)" stroke-width="4"/></svg>
  Werden Sie Vereinsmitglied
</h2>
<div class="abs kicker" style="left:69px;top:1520px">PROJEKT UNTERSTÜTZEN UND VEREINSMITGLIED WERDEN</div>
<div class="abs member-text">
  <p>Lorem ipsum dolor sit amet, eu sed nulla imperdiet complectitur, dico philosophia eu vel, dicunt maluisset imperdiet et eos. At usu verterem partiendo consetetur, id nullam laboramus nec. Et paulo nobis integre sit, qui ludus option periculis id.</p>
  <p>Fierent incorrupte no qui. Vide invenire mediocritatem duo et.Everti appetere eos et. Vel viris verterem ex, mollis iriure feugiat eum eu. Ea pro corpora percipitur, brute nemore ei eum. Iuvaret partiendo laboramus te pri, in per enim nominavi, eligendi inciderint ea vix. Wisi erat an ius.Id feugiat recteque vim, ex oratio epicuri elaboraret duo.</p>
  <p><strong>Eine Vereinsmitgliedschaft ist derzeit noch kostenlos.<br>Sie unterstützen den Verein damit ideell.</strong></p>
</div>
<div class="abs kicker" style="left:744px;top:1520px">ANMELDEFORMULAR</div>
<div class="abs field" style="left:744px;top:1557px;width:257px">Name</div>
<div class="abs field" style="left:744px;top:1605px;width:257px">Vorname</div>
<div class="abs field" style="left:744px;top:1653px;width:257px">Strasse / Nr.</div>
<div class="abs field" style="left:744px;top:1701px;width:60px">PLZ</div>
<div class="abs field" style="left:744px;top:1750px;width:257px">Ort</div>
<div class="abs field" style="left:744px;top:1798px;width:257px">E-Mail Adresse</div>
<div class="abs btn small-btn" style="left:744px;top:1846px;width:73px">SENDEN</div>

<section class="abs sponsor-band"></section>
<h2 class="abs sec-title" style="top:2002px">
  <svg width="48" height="26" viewBox="0 0 48 26" aria-hidden="true"><path d="M7 3a5 5 0 0 1 8 3h18a5 5 0 1 1 8 4 5 5 0 0 1 0 6 5 5 0 1 1-8 4H15a5 5 0 1 1-8-4 5 5 0 0 1 0-6 5 5 0 0 1 0-7z" fill="none" stroke="var(--orange)" stroke-width="4"/></svg>
  Werden Sie Sponsor
</h2>
<div class="abs kicker" style="left:0;top:2045px;width:1200px;text-align:center">HELFEN SIE UNS DIESES PROJEKT ZU VERWIRKLICHEN</div>
<div class="abs logo-box" style="left:99px">Pfotenküche</div>
<div class="abs logo-box empty" style="left:327px;width:96px">HIER KÖNNTE<br>IHR LOGO<br>STEHEN</div>
<div class="abs logo-box" style="left:536px;width:107px">Napfzeit</div>
<div class="abs logo-box" style="left:754px">Fellgut</div>
<div class="abs logo-box" style="left:983px;top:2125px;height:54px">Nobelfutter</div>

<h2 class="abs sec-title" style="top:2320px">
  <svg width="48" height="28" viewBox="0 0 48 28" aria-hidden="true"><rect x="2" y="2" width="44" height="24" fill="var(--orange)" stroke="var(--orange-soft)" stroke-width="2"/><ellipse cx="24" cy="14" rx="9" ry="7" fill="#fff"/></svg>
  Spenden
</h2>
<div class="abs bank">
  <b>SPENDENKONTO:</b> KATZENHAIN OBERLAU<br>
  <b>IBAN:</b> 98 00000 00000 00000 9<br>
  <b>BIC:</b> 6553873
</div>
<div class="abs pay" style="left:401px"><span class="pay-mark"></span>Zahlfix</div>
<div class="abs pay" style="left:486px"><span class="pay-mark"></span>Giroflink</div>
<div class="abs pay" style="left:583px"><span class="pay-mark"></span>Netzbeutel</div>
<div class="abs pay-slip">EINZAHLUNGSSCHEIN</div>

<section class="abs photo contact-photo" role="img" aria-label="Foto einer Hand, die eine Hundepfote hält"></section>
<h2 class="abs contact-title">Wir freuen uns auf Ihre Anregungen &amp; Ideen</h2>

<div class="abs field" style="left:289px;top:2929px;width:307px">Name</div>
<div class="abs field" style="left:289px;top:2964px;width:307px">E-Mail Adresse</div>
<div class="abs field" style="left:639px;top:2929px;width:307px;height:62px">Ihr Text</div>
<div class="abs" style="left:289px;top:3001px;display:flex;align-items:center;gap:7px;font-size:9px;color:#666">
  <span style="width:9px;height:9px;border:1px solid #aaa;display:inline-block"></span>Kopie an meine E-Mail Adresse
</div>
<div class="abs btn small-btn" style="left:289px;top:3031px;width:67px">SENDEN</div>

<footer class="abs footer">info@katzenhain-oberlau.ch</footer>
</body>
</html>
```